CEO Survey Report Landing Page - lead response

Looking for responsive design landing page done in modern elegant style that will appeal to the top executive (CEO) of big businesses. This page should collect first name, last name, business email and have download button. we require source file in both adobe photoshop psd and indesign (idd).

Example of landing page: https://blog.plimvora.example/post/552810937461/how-to-design-an-optimized-ebook-landing-page (see attachments for more examples)

Target Market(s)

CEO - top executive of US business between 100 million to 1 billion a year in revenue

Number of Pages Required

1 page

Font styles to use
Sans Serif

Colors
0692cd
ffffff
f78f20
9bcb3b

Requirements
Must have
• place the copy text given in the doc on the page. we are focusing on 1. meaning of copy text being powerful and easy to understand. 2. a way to highlight the 3 numeric values with text . 3. clear call to action.
Nice to have
• idea 1. see the 3 numbers with a graphic. consider for example like put each number in a circle with label below.
• optional idea 2. perhaps consider an elegant business info-graphic look
• optional idea 3. as an option consider screened gradient color in blue /green or photo with translucent layer - behind make white / light gray main area where have copy etc.
Should not have
• do NOT make this look like a regular website. see the plimvora link and sample reference of landing page designs. it should be a landing page with clear easy elegant form with a lot of clear space.
• have cluttered looks. photo images of people in the foreground etc that distracts is bad. a screened back photo in the background is fine.

```html
<!DOCTYPE html>
<html lang="en">
<head>
<meta charset="utf-8">
<title>Crestline Netcom – CEO Cloud Survey</title>
<link href="https://fonts.googleapis.com/css2?family=Montserrat:wght@400;700&family=Roboto:ital,wght@0,400;0,500;0,700;1,400&display=swap" rel="stylesheet">
<style>
  :root{
    --brand-blue:#0692cd;
    --bright-blue:#0a9bf2;
    --deep-blue:#0a78c8;
    --orange:#f78f20;
    --green:#9bcb3b;
    --ink:#3c3c3c;
    --muted:#666;
    --field:#f6f6f6;
    --pale:#f3f7fc;
    --bar-green:#a4c51a;
    --bar-sky:#80cfe8;
    --bar-yellow:#f0d300;
    --bar-orange:#f28500;
    --bar-plum:#6f236f;
    --bar-blue:#1ba1e2;
  }
  *{box-sizing:border-box;margin:0;padding:0}
  html,body{width:677px;height:1200px;overflow:hidden;background:#fff}
  .page{position:relative;width:677px;height:1200px;overflow:hidden;font-family:'Roboto',sans-serif;color:var(--ink)}
  .abs{position:absolute}
  .backdrop{position:absolute;left:0;top:0}
  .brand{left:74px;top:10px;display:flex;align-items:center;gap:6px;font-family:'Montserrat',sans-serif;font-size:13px;color:var(--deep-blue)}
  .brand-dot{width:18px;height:18px;border-radius:50%;background:var(--bright-blue)}
  .hero-title{left:74px;top:72px;font-family:'Montserrat',sans-serif;font-weight:400;font-size:23px;line-height:30px;color:var(--ink)}
  .hero-title b,.read-title b,.section-title b{font-weight:700}
  .hero-sub{left:74px;top:140px;font-family:'Montserrat',sans-serif;font-size:12.5px;color:var(--ink)}
  .btn{display:flex;align-items:center;justify-content:center;background:var(--deep-blue);color:#fff;font-weight:700;font-size:8.5px;letter-spacing:.4px;border-radius:3px;text-transform:uppercase}
  .btn-survey{left:74px;top:170px;width:177px;height:27px}
  .lead-card{left:381px;top:50px;width:214px;height:194px;background:#fff;border-radius:5px;box-shadow:0 6px 24px rgba(0,60,120,.12);padding:0 19px}
  .lead-card h2{margin-top:19px;font-family:'Montserrat',sans-serif;font-weight:400;font-size:11.5px;color:var(--ink)}
  .lead-card h2 span{color:var(--bright-blue);font-weight:700}
  .field{height:27px;margin-top:5px;border-radius:3px;background:var(--field);font-size:8px;color:#c6c6c6;display:flex;align-items:center;padding-left:10px}
  .field:first-of-type{margin-top:12px}
  .field.active{background:#fff;border:1px solid #ddd;color:#888}
  .btn-download{height:27px;margin-top:12px}
  .stat{width:160px;text-align:center}
  .stat svg{display:block;margin:0 auto}
  .stat-num{font-family:'Montserrat',sans-serif;font-weight:700;font-size:17px;color:#111;margin-top:8px}
  .stat-label{font-size:8.8px;color:#444;margin-top:2px}
  .stat-note{font-size:7.4px;color:#555;margin-top:4px}
  .read-title{left:113px;top:498px;width:215px;white-space:nowrap;font-family:'Montserrat',sans-serif;font-weight:400;font-size:16px;line-height:21px;color:var(--ink)}
  .btn-report{left:114px;top:561px;width:177px;height:27px}
  .report-book{left:382px;top:428px;width:200px;height:232px;border-radius:4px;background:linear-gradient(135deg,#3aa0e0 0%,#dde7ef 45%,#f1f2f4 100%);opacity:.85}
  .report-rock{left:327px;top:592px;width:98px;height:68px;border-radius:50%;background:radial-gradient(circle at 40% 40%,#cfcac6,#8d8784);opacity:.8}
  .section-title{left:0;width:677px;top:735px;text-align:center;font-family:'Montserrat',sans-serif;font-weight:400;font-size:16px;color:#333}
  .chart{left:0;top:773px;width:677px}
  .row{position:relative;height:18px}
  .row-label{position:absolute;right:417px;top:0;font-size:7.2px;color:#444;line-height:10px;white-space:nowrap}
  .row-bar{position:absolute;left:270px;top:0;height:10px}
  .row-pct{position:absolute;left:509px;top:0;font-size:7.2px;color:#333;line-height:10px}
  .quote{left:219px;width:238px;top:1048px;text-align:center;font-style:italic;font-size:9.4px;line-height:15.2px;color:#666}
  .qmark{top:1036px;font-family:'Montserrat',sans-serif;font-weight:700;font-size:38px;color:#a7d4f5;line-height:1}
  .rule{left:329px;top:1101px;width:13px;height:1.5px;background:var(--bright-blue)}
  .author{left:0;width:677px;top:1113px;text-align:center;font-weight:500;font-size:8.8px;color:var(--deep-blue)}
  .copyright{left:0;width:677px;top:1172px;text-align:center;font-family:'Montserrat',sans-serif;font-size:6.8px;color:#999}
</style>
</head>
<body>
<main class="page">
  <svg class="backdrop" width="677" height="1200" aria-hidden="true">
    <defs>
      <linearGradient id="paleWash" x1="0" y1="0" x2="1" y2="1">
        <stop offset="0" stop-color="#f1f6fc"/><stop offset="1" stop-color="#fbfdff"/>
      </linearGradient>
    </defs>
    <path d="M0 0 H420 V240 L330 275 H110 Q70 275 50 230 L0 120 Z" fill="url(#paleWash)"/>
    <path d="M70 440 L330 420 L677 560 V880 L380 960 Q330 975 290 955 L30 820 L0 760 V500 Z" fill="url(#paleWash)" opacity=".8"/>
    <path d="M0 890 Q60 830 220 870 L677 980 V1050 L360 1160 Q320 1170 280 1150 L0 980 Z" fill="url(#paleWash)" opacity=".7"/>
    <path d="M416 32 Q416 0 448 0 H677 V216 L584 272 Q568 280 552 272 L504 244 L416 200 Z" fill="var(--bright-blue)"/>
    <path d="M385 215 L414 200 L414 262 L385 276 L356 262 L356 228 Z" fill="var(--deep-blue)"/>
    <path d="M238 212 Q230 250 290 246 Q320 242 336 232" fill="none" stroke="#cfd6dc" stroke-width="1"/>
    <path d="M328 228 L337 232 L330 239" fill="none" stroke="#cfd6dc" stroke-width="1"/>
    <path d="M188 608 Q180 650 250 644 Q275 641 286 636" fill="none" stroke="#cfd6dc" stroke-width="1"/>
    <path d="M278 632 L287 636 L280 643" fill="none" stroke="#cfd6dc" stroke-width="1"/>
  </svg>

  <div class="abs brand"><span class="brand-dot"></span>Crestline Netcom</div>

  <h1 class="abs hero-title">John <b>achieve</b> your<br><b>objectives</b> easier</h1>
  <p class="abs hero-sub">Reduce Cloud Friction. Get more done</p>
  <a class="abs btn btn-survey">Get the 2018 CEO Cloud Survey</a>

  <form class="abs lead-card">
    <h2>Claim your <span>free e-book!</span></h2>
    <div class="field active">First Name</div>
    <div class="field">Last Name</div>
    <div class="field">Email Address</div>
    <div class="btn btn-download">Download Now</div>
  </form>

  <div class="abs stat" style="left:96px;top:300px">
    <svg width="48" height="54" viewBox="0 0 48 54"><path d="M24 0 L47 13 V41 L24 54 L1 41 V13 Z" fill="var(--bright-blue)"/>
      <g fill="none" stroke="#fff" stroke-width="1.3"><circle cx="18" cy="24" r="3.5"/><circle cx="30" cy="24" r="3.5"/><circle cx="24" cy="21" r="3.5"/><path d="M12 36 Q12 29 18 29 Q24 29 24 36 M24 36 Q24 29 30 29 Q36 29 36 36 M17 33 Q17 26 24 26 Q31 26 31 33"/></g></svg>
    <div class="stat-num">5000</div>
    <div class="stat-label">CEOs Of US Mid-Sized Companies</div>
  </div>
  <div class="abs stat" style="left:263px;top:300px">
    <svg width="48" height="54" viewBox="0 0 48 54"><path d="M24 0 L47 13 V41 L24 54 L1 41 V13 Z" fill="var(--green)"/>
      <g fill="none" stroke="#fff" stroke-width="1.3"><path d="M19 30 Q15 26 16 22 Q18 16 24 16 Q30 16 32 22 Q33 26 29 30 V34 H19 Z"/><path d="M20 37 H28 M22 34 V27 M26 34 V27 M24 10 V12 M14 15 L16 17 M34 15 L32 17"/></g></svg>
    <div class="stat-num">06</div>
    <div class="stat-label">Things To Know</div>
    <div class="stat-note">Cloud Pitfalls, Areas To Watch Out</div>
  </div>
  <div class="abs stat" style="left:430px;top:300px">
    <svg width="48" height="54" viewBox="0 0 48 54"><path d="M24 0 L47 13 V41 L24 54 L1 41 V13 Z" fill="var(--orange)"/>
      <g fill="none" stroke="#fff" stroke-width="1.3"><rect x="13" y="25" width="5" height="11"/><path d="M18 26 L23 20 Q24 15 27 16 Q28 19 26 24 H33 Q35 25 34 28 L32 34 Q31 36 29 36 H18"/></g></svg>
    <div class="stat-num">06</div>
    <div class="stat-label">Recommendations</div>
  </div>

  <h2 class="abs read-title">A quick <b>10 minute</b> read to<br>succeed better with <b>Cloud.</b></h2>
  <a class="abs btn btn-report">Download the Report Now!</a>
  <div class="abs report-rock" role="img" aria-label="Rough mineral rock"></div>
  <div class="abs report-book" role="img" aria-label="Printed CEO Level Cloud Survey 2018 report booklet leaning upright"></div>

  <h2 class="abs section-title">Cloud <b>Concerns</b></h2>
  <div class="abs chart">
    <div class="row"><span class="row-label">Tax on executive time to oversee</span><span class="row-bar" style="width:160px;background:var(--bar-green)"></span><span class="row-pct">53%</span></div>
    <div class="row"><span class="row-label">Worry about team execution</span><span class="row-bar" style="width:181px;background:var(--bar-sky)"></span><span class="row-pct">65%</span></div>
    <div class="row"><span class="row-label">Cost</span><span class="row-bar" style="width:197px;background:var(--bar-yellow)"></span><span class="row-pct">70%</span></div>
    <div class="row"><span class="row-label">Security</span><span class="row-bar" style="width:230px;background:var(--bar-orange)"></span><span class="row-pct">81%</span></div>
    <div class="row"><span class="row-label">Keep pace with Cloud evolution</span><span class="row-bar" style="width:168px;background:var(--bar-plum)"></span><span class="row-pct">57%</span></div>
    <div class="row"><span class="row-label">Retention of Cloud talent</span><span class="row-bar" style="width:58px;background:var(--bar-blue)"></span><span class="row-pct">20%</span></div>
  </div>

  <svg class="abs" style="left:302px;top:966px" width="68" height="76" viewBox="0 0 68 76">
    <path d="M34 0 L67 19 V57 L34 76 L1 57 V19 Z" fill="var(--deep-blue)"/>
    <path d="M34 6 L61 22 V54 L34 70 L7 54 V22 Z" fill="#b7c2cc" role="img" aria-label="Portrait photo of the quoted executive"/>
  </svg>
  <span class="abs qmark" style="left:184px">“</span>
  <p class="abs quote">This CEO Cloud Report helped my team gain critical insight and helped us cut weeks of our time. No doubt it save me a few headaches.</p>
  <span class="abs qmark" style="left:470px">”</span>
  <div class="abs rule"></div>
  <div class="abs author">Daniel Orwick</div>

  <footer class="abs copyright">© Copyright 2018 Crestlinenetcom</footer>
</main>
</body>
</html>
```